Vision Pamphlet to attract more patients

We need a modern pamphlet design for our company Lumen Plan.
size 5.5 x8.5"
Half Fold, Front and back
Colors: Sky blue, white, green, splash of yellow

Easy to understand bullet points

Front page (Welcome to GRASP THE HOUR ) Office logo
Details on Oculor Lumen Plan and financing options

page 2 , 3 ( inside fold)

Irisa Family Lumen Plan

Family plan: $79 annual fee for your entire family

Individual plan: $49 annual fee for each individual

ALL MEMBERSHIP BENEFITS
Member receives 30% off all of the following :
eye exam, Glaucoma exam, contact lens exam, frame, prescription lenses and sunglasses

ADDITIONAL BENEFITS
$25 off Red eye treatment
$50 off Dry eye Treatment
$100 towards LASIK procedure
$100 towards ORthoK treatment

page 4 ( back)
Frequently Asked Question
Q. How can I use my membership?
A. Once you enroll you can use your benefits right away.

Q. How many family can I enroll?
A. This family plan is intended for parents and children in one immediate family.

Q. How can I keep my membership current
A. As long as you pay your annual membership you will automatically have active membership

Q. How many times can I use my benefits a year?
A. You can use it all year long.

Q. Will i receive special financing options?
A. We offer pay bridge that can give you flexible, budget-friendly choices when selecting your financing terms.

OCULOR INFORMATION
4863 MARLOW AVE
RESEDA CA 90418
818.602.7394.
www.oculorview.example

Target Market(s)

young individuals and family

Industry/Entity Type

It Company

Font styles to use
Sans Serif

Colors
33a6d7
33b8a4
886aae
fbee3d
0655a3
9bcb3b
ffffff
f37122

Requirements
Must have
• photo of glasses, eye doctor,
• Pay Bridge logo at the bottom of Frequently Asked Questions
Nice to have
• easy to read design, eye catching

```html
<!DOCTYPE html>
<html lang="en">
<head>
<meta charset="utf-8">
<title>Irisa Family Lumen Plan – Inside Spread</title>
<link href="https://fonts.googleapis.com/css2?family=Oswald:wght@400;500;600;700&family=Roboto+Condensed:wght@400;700&family=Open+Sans:wght@400;600;700&display=swap" rel="stylesheet">
<style>
:root{
  --sky:#33a6d7;
  --navy:#0655a3;
  --deep:#0a3f86;
  --yellow:#fbee3d;
  --gold:#ffd21f;
  --green:#9bcb3b;
  --teal:#33b8a4;
  --white:#ffffff;
  --ink:#1b2b4a;
  --mist:#e9eef3;
}
*{box-sizing:border-box;margin:0;padding:0}
html,body{width:1200px;height:777px;overflow:hidden;background:#fff}
.spread{position:relative;width:1200px;height:777px;overflow:hidden;font-family:"Open Sans",Arial,sans-serif}

/* left hero */
.hero-photo{position:absolute;left:0;top:0;width:600px;height:615px;
  background:radial-gradient(ellipse at 32% 45%,#c99a7d 0%,#8f6a58 22%,transparent 42%),
  linear-gradient(135deg,#3b4144 0%,#6f7a7e 40%,#c9c6c2 70%,#e4d7d6 100%)}
.plan{position:absolute;top:498px;height:80px;border-radius:8px;padding:6px 10px 0 12px;
  box-shadow:0 2px 6px rgba(0,0,0,.25)}
.plan h3{font-family:"Oswald",sans-serif;font-weight:600;font-size:25px;line-height:28px;letter-spacing:.5px;border-bottom:2px solid currentColor;padding-bottom:1px}
.plan .row{display:flex;align-items:center;gap:8px;margin-top:2px}
.plan .price{font-family:"Oswald",sans-serif;font-weight:600;font-size:42px;line-height:40px}
.plan .desc{font-family:"Roboto Condensed",sans-serif;font-size:16px;line-height:17px;text-transform:uppercase}
.plan--family{left:37px;width:262px;background:var(--sky);color:var(--white)}
.plan--family h3 span{color:var(--yellow)}
.plan--family h3{border-color:var(--white)}
.plan--individual{left:310px;width:265px;background:var(--gold);color:var(--navy)}

/* benefits panel */
.benefits{position:absolute;left:600px;top:0;width:600px;height:348px;
  background:linear-gradient(180deg,#1f8ad8 0%,#0c6fc9 60%,#0a62bd 100%);color:var(--white);text-align:center}
.benefits h2{font-family:"Oswald",sans-serif;font-weight:600;font-size:27px;letter-spacing:1px;margin-top:24px;line-height:32px}
.benefits h2 .hi{color:var(--yellow)}
.benefits h2 .lo{font-weight:400}
.benefits .rule{width:310px;height:2px;background:var(--white);margin:2px auto 0}
.benefits p{font-size:17px;margin-top:3px}
.benefits p b{color:var(--yellow)}
.grid{position:absolute;left:45px;top:103px;width:510px;display:grid;grid-template-columns:repeat(3,170px);row-gap:10px}
.item{display:flex;flex-direction:column;align-items:center}
.item svg{width:58px;height:58px;stroke:var(--white);fill:none;stroke-width:2.6;stroke-linecap:round;stroke-linejoin:round}
.item span{font-family:"Roboto Condensed",sans-serif;font-size:16px;line-height:17px;margin-top:6px;text-transform:uppercase}
.item b{color:var(--yellow);font-weight:700}

/* additional */
.additional{position:absolute;left:600px;top:348px;width:600px;height:267px;
  background:linear-gradient(180deg,#f2f5f8 0%,#e6ecf1 100%)}
.additional h2{font-family:"Oswald",sans-serif;font-weight:600;font-size:24px;color:var(--ink);text-align:center;margin-top:6px;letter-spacing:.5px}
.additional h2 span{color:var(--navy)}
.additional .rule{width:250px;height:2px;background:var(--ink);margin:0 auto}
.offer{position:absolute}
.tag{position:absolute;background:var(--gold);color:#111;font-family:"Oswald",sans-serif;font-weight:700;font-size:32px;line-height:44px;padding:0 6px;box-shadow:2px 2px 4px rgba(0,0,0,.3);white-space:nowrap}
.tag small{font-size:14px;font-weight:600}
.ribbon{position:absolute;background:linear-gradient(180deg,#2e9be0,var(--navy));color:var(--white);font-family:"Oswald",sans-serif;font-weight:500;font-size:19px;line-height:38px;text-align:center;text-transform:uppercase;white-space:nowrap;box-shadow:0 3px 5px rgba(0,0,0,.25)}
.ribbon::after{content:"";position:absolute;bottom:-10px;border-top:10px solid var(--green)}
.ribbon.fold-left::after{left:0;border-left:12px solid transparent}
.ribbon.fold-right::after{right:0;border-right:12px solid transparent}

/* bottom band */
.stripe{position:absolute;top:615px;height:22px}
.stripe--blue{left:0;width:400px;background:var(--navy)}
.stripe--yellow{left:400px;width:400px;background:#f6b51d}
.stripe--green{left:800px;width:400px;background:var(--green)}
.gallery{position:absolute;left:0;top:637px;width:1200px;height:140px;display:flex}
.tile{height:100%}
.tile--blue{background:linear-gradient(90deg,#0a5fa8,#2aa0db)}
.tile--photo{background:linear-gradient(135deg,#d9d9d9,#8d9398)}
.tile--dark{background:linear-gradient(135deg,#5c6369,#2b2f33)}
</style>
</head>
<body>
<main class="spread">

  <section class="hero-photo" role="img" aria-label="Photo of a smiling young girl wearing glasses in a classroom"></section>

  <div class="plan plan--family">
    <h3><span>FAMILY</span> PLAN:</h3>
    <div class="row"><span class="price">$79</span><span class="desc">Annual fee for<br>your entire family</span></div>
  </div>
  <div class="plan plan--individual">
    <h3><span>INDIVIDUAL</span> PLAN:</h3>
    <div class="row"><span class="price">$49</span><span class="desc">Annual fee for<br>each individual</span></div>
  </div>

  <section class="benefits">
    <h2><span class="hi">ALL MEMBERSHIP</span> <span class="lo">BENEFITS</span></h2>
    <div class="rule"></div>
    <p>Member receives <b>30% off</b> all of the following :</p>
    <div class="grid">
      <div class="item">
        <svg viewBox="0 0 60 60"><path d="M6 30c7-10 15-15 24-15s17 5 24 15c-7 10-15 15-24 15S13 40 6 30z"/><circle cx="30" cy="30" r="8"/><path d="M30 4v10M30 46v10M4 30h6M50 30h6"/></svg>
        <span><b>Eye</b> exam</span>
      </div>
      <div class="item">
        <svg viewBox="0 0 60 60"><path d="M6 32c7-11 15-16 24-16s17 5 24 16c-7 10-15 14-24 14S13 42 6 32z"/><circle cx="30" cy="31" r="9"/><path d="M14 18l-4-6M22 14l-2-7M30 13V6M38 14l2-7M46 18l4-6"/></svg>
        <span><b>Glaucoma</b><br>exam</span>
      </div>
      <div class="item">
        <svg viewBox="0 0 60 60"><ellipse cx="24" cy="30" rx="10" ry="18"/><ellipse cx="37" cy="30" rx="10" ry="18"/><path d="M20 18c-3 6-3 18 0 24M33 18c-3 6-3 18 0 24"/></svg>
        <span><b>Contact lens</b><br>exam</span>
      </div>
      <div class="item">
        <svg viewBox="0 0 60 60"><path d="M5 24h20c0 10-4 15-10 15S5 34 5 24zM35 24h20c0 10-4 15-10 15s-10-5-10-15zM25 26c3-2 7-2 10 0M5 24l-2-2M55 24l2-2"/></svg>
        <span><b>Frames</b></span>
      </div>
      <div class="item">
        <svg viewBox="0 0 60 60"><path d="M14 6h24l8 8v40H14z"/><path d="M20 20h16M20 28h16M20 36h10"/><path d="M48 20l6 6-16 16-7 1 1-7z"/></svg>
        <span><b>Prescription</b><br>lenses</span>
      </div>
      <div class="item">
        <svg viewBox="0 0 60 60"><path d="M4 24h22c0 10-4 14-11 14S4 34 4 24zM34 24h22c0 10-4 14-11 14s-11-4-11-14zM26 26c3-2 5-2 8 0" fill="#fff"/></svg>
        <span><b>Sun</b>glasses</span>
      </div>
    </div>
  </section>

  <section class="additional">
    <h2><span>ADDITIONAL</span> BENEFITS</h2>
    <div class="rule"></div>

    <div class="tag" style="left:82px;top:57px">$25<small>OFF</small></div>
    <div class="ribbon fold-left" style="left:60px;top:100px;width:225px">Red Eye Treatment</div>

    <div class="tag" style="left:52px;top:137px">$50<small>OFF</small></div>
    <div class="ribbon fold-left" style="left:22px;top:180px;width:240px">Dry Eye Treatment</div>

    <div class="tag" style="left:423px;top:60px">$100<small>OFF</small></div>
    <div class="ribbon fold-right" style="left:307px;top:104px;width:228px">Towards Lasik Procedure</div>

    <div class="tag" style="left:447px;top:139px">$100<small>OFF</small></div>
    <div class="ribbon fold-right" style="left:328px;top:186px;width:236px;font-size:17px">Towards Orthok Treatment</div>
  </section>

  <div class="stripe stripe--blue"></div>
  <div class="stripe stripe--yellow"></div>
  <div class="stripe stripe--green"></div>

  <section class="gallery">
    <div class="tile tile--blue" style="width:50px"></div>
    <div class="tile tile--photo" style="width:170px" role="img" aria-label="Photo of a mother with her two daughters wearing glasses"></div>
    <div class="tile tile--blue" style="width:140px" role="img" aria-label="Photo of round eyeglasses on a blue background"></div>
    <div class="tile tile--photo" style="width:210px" role="img" aria-label="Photo of the eye care team standing in the office"></div>
    <div class="tile tile--blue" style="width:40px"></div>
    <div class="tile tile--photo" style="width:200px" role="img" aria-label="Photo of black eyeglass frames"></div>
    <div class="tile tile--blue" style="width:40px"></div>
    <div class="tile tile--dark" style="width:140px" role="img" aria-label="Photo of a smiling couple wearing glasses"></div>
    <div class="tile tile--blue" style="width:60px"></div>
    <div class="tile tile--photo" style="width:150px" role="img" aria-label="Photo of thick black eyeglass frames"></div>
  </section>

</main>
</body>
</html>
```